Help make our corporate website modern and cool with graphical elements and icons

We are makers of cloud infrastructure software (www.nimbrotek.com) and our target audience is developers. Developers generally want text and icons, they don't care for photos. They want good usability and easy-to-find information. Think forkhive.com, cloud.zephyrqa.com, www.stackmoor.com, pallork.com for reference.

Your challenge will be to modernize the site and make it look "cool" from a developer's point-of-view while still keeping the basic site structure. You can add graphical elements that make the pages come more alive, suggest different layout options, and incorporate icons that we've recently developed (I've attached them for your review). We will keep the Nimbrotek blue and gray, but you are free to add complementary colors in your designs to help spice up the page. See the complementary colors we've used in the icons package.

A successful design will keep the core identity of our website but will make the pages more exciting and compelling to visit, and make the visitor want to scroll and click to dive in deeper into the site. I also want to see additional mock-ups for the main landing pages (Why Nimbrotek, Products, Community, and a new landing page for Resources).

We use WordPress and the Q theme, so if you have familiarity with that theme and its capabilities, even better.

Target Market(s)

Mobile and Web application developers from larger organizations. Developers typically don't like stock images of people or landscapes, they usually just want the information they're looking for presented in a clean and organized way. That said, they do like it if an icon or design element helps them visualize the information. So the design should be useful and necessary to the info provided.

Industry/Entity Type

Computer Software

Number of Pages Required

5+ page

Font styles to use
Sans Serif
Other font styles liked:
• We use Lato as our main font

Colors

Designer to choose colors to be used in the design.

Requirements
Must have
• Must haves:
• - clean and modern design, not too busy but still visually engaging
• - keep the core identity of the site while adding graphical elements/icons
• - use either the hexagons from the icons or incorporate the venn diagram shape somehow from https://www.nimbrotek.com/why-nimbrotek/
• - shapes and icons are preferred over photos or stock "tech" images
• - should keep the nimbrotek blue and gray but can have complementary accent colors (see the icon colors that I've attached)
• - you can use the attached icons
• - make the information appealing to view, scroll and click through
• - design must not interfere with navigation or readability, must complement and be appropriate for the specific information shown
• - use pallork.com and cloud.zephyrqa.com for reference
Nice to have
• nice to haves:
• - familiarity with Zephyrqa Run Engine and cloud computing
• - easy to implement on WordPress, familiarity with Q theme a plus
• - ability to identify with app developers
Should not have
• - unfortunately, stock photos of people or landscapes won't work
• - don't use clip art of clouds or other stock images of high tech
• - don't make it too busy, we are looking for clean and modern

```html
<!DOCTYPE html>
<html lang="en">
<head>
<meta charset="utf-8">
<title>Nimbrotek — Multi cloud native</title>
<link href="https://fonts.googleapis.com/css2?family=Lato:wght@300;400;700;900&display=swap" rel="stylesheet">
<style>
:root{
  --blue:#1ba1e2;
  --blue-dark:#0f86c4;
  --ink:#2c3a47;
  --gray:#5d6b78;
  --gray-light:#eef1f4;
  --line:#d6dde3;
  --navy:#22303d;
  --navy-deep:#1a2530;
  --white:#ffffff;
}
*{box-sizing:border-box;margin:0;padding:0}
html,body{width:1200px;height:2848px;overflow:hidden}
body{font-family:"Lato",Arial,sans-serif;color:var(--ink);background:var(--white);position:relative}
section,header,footer{position:absolute;left:0;width:1200px}
h2{font-weight:700;font-size:34px;line-height:1.3;text-align:center;color:var(--ink)}

/* nav */
.site-nav{top:0;height:56px;background:var(--blue);display:flex;align-items:center;padding:0 40px}
.brand{display:flex;align-items:center;gap:10px;color:var(--white);font-weight:900;font-size:28px}
.brand-mark{width:22px;height:22px;background:var(--white);border-radius:50%}
.menu{margin-left:auto;display:flex;gap:28px;list-style:none}
.menu li{color:var(--white);font-size:13px;font-weight:700;letter-spacing:.5px}

/* hero */
.hero{top:56px;height:484px;text-align:center;color:var(--white);overflow:hidden}
.hero-bg{position:absolute;inset:0;background:radial-gradient(ellipse at 60% 30%,#2d4a66 0%,#152a3f 55%,#0b1725 100%)}
.hero-content{position:relative;padding-top:60px}
.hero h1{font-weight:900;font-size:46px;line-height:1.2}
.hero p{font-size:17px;line-height:1.55;max-width:640px;margin:22px auto 0;color:#d5e2ee}
.hero-actions{margin-top:30px;display:flex;justify-content:center;gap:20px}
.btn{display:inline-block;height:46px;line-height:46px;padding:0 36px;font-size:15px;font-weight:700;border-radius:3px}
.btn-primary{background:var(--blue);color:var(--white)}
.btn-ghost{border:2px solid var(--white);color:var(--white);line-height:42px}
.cloud-partners{position:relative;margin-top:70px;display:flex;justify-content:center;gap:62px}
.partner{display:flex;flex-direction:column;align-items:center;gap:10px;font-size:14px;font-weight:700;color:var(--white)}
.partner-shape{width:38px;height:38px;border-radius:50%;background:rgba(255,255,255,.85)}

/* portability */
.portability{top:540px;height:420px;background:var(--gray-light)}
.portability h2{margin-top:62px}
.feature-cards{display:flex;justify-content:center;gap:58px;margin-top:44px}
.phone-card{width:170px;height:200px;border:3px solid var(--gray);border-bottom:none;border-radius:22px 22px 0 0;background:var(--white);display:flex;flex-direction:column;align-items:center;padding-top:26px}
.phone-card .screen{width:130px;height:120px;border:1px solid var(--line);display:flex;flex-direction:column;align-items:center;justify-content:center;gap:14px}
.phone-card .label{font-weight:700;font-size:14px}

/* benefits */
.benefits{top:960px;height:420px}
.benefits h2{margin-top:40px;color:var(--blue-dark);font-size:32px;padding:0 140px}
.benefit-map{position:absolute;left:0;top:150px}

/* calculator */
.calculator{top:1380px;height:320px;display:flex}
.calc-info{width:520px;background:var(--gray-light);padding:60px 60px 0 100px}
.calc-info h3{font-size:28px;font-weight:900;line-height:1.2}
.calc-info p{font-size:13px;color:var(--gray);line-height:1.6;margin-top:16px}
.calc-chart{width:680px;background:var(--blue);position:relative}

/* steps */
.steps{top:1760px;height:320px}
.steps h2{margin-top:10px;font-size:32px}
.step-list{display:flex;justify-content:center;gap:50px;margin-top:36px}
.step{width:290px;display:flex;gap:16px}
.step-icon{flex:none;width:44px;height:44px;border-radius:50%;background:var(--blue);display:flex;align-items:center;justify-content:center}
.step h4{font-size:15px;font-weight:900;letter-spacing:.3px}
.step p{font-size:12px;color:var(--gray);line-height:1.55;margin-top:8px}
.steps .btn{position:absolute;left:50%;transform:translateX(-50%);top:218px;height:40px;line-height:40px;font-size:13px;padding:0 30px}

/* testimonials */
.testimonials{top:2080px;height:320px;display:flex}
.quote-panel{width:400px;background:var(--blue);color:var(--white);padding:44px 60px 0 60px}
.quote-panel h3{font-size:28px;font-weight:900}
.quote-panel blockquote{font-size:14px;line-height:1.6;margin-top:28px;font-style:italic}
.quote-panel cite{display:block;font-style:normal;font-size:12px;font-weight:700;margin-top:18px}
.quote-nav{display:flex;gap:8px;margin-top:26px}
.quote-nav span{width:28px;height:28px;border:1px solid var(--white);display:flex;align-items:center;justify-content:center}
.video-frame{width:800px;position:relative;background:linear-gradient(135deg,#7f8c96 0%,#b9c3ca 50%,#6c7984 100%)}
.play{position:absolute;left:370px;top:130px;width:60px;height:60px}
.speaker{position:absolute;left:40px;bottom:30px;color:var(--white)}
.speaker strong{display:block;font-size:30px;font-weight:900;letter-spacing:1px}
.speaker span{font-size:14px;font-weight:700;letter-spacing:1px}

/* clients */
.clients{top:2400px;height:180px}
.clients h2{font-size:22px;margin-top:28px}
.client-row{display:flex;justify-content:center;gap:90px;margin-top:40px}
.client{display:flex;align-items:center;gap:8px;font-size:26px;font-weight:900;color:var(--ink)}
.client i{width:14px;height:14px;background:var(--ink);display:block}

/* footer */
.site-footer{top:2580px;height:268px;display:flex;background:var(--navy)}
.contact-form{width:400px;background:var(--navy-deep);padding:28px 60px 0 60px;color:var(--white)}
.contact-form h3{font-size:18px;font-weight:700;margin-bottom:14px}
.field{height:24px;background:var(--white);margin-bottom:8px;font-size:11px;color:#8a96a0;padding:5px 8px}
.field.tall{height:40px}
.submit{display:inline-block;background:var(--blue);color:var(--white);font-size:11px;font-weight:700;padding:7px 16px}
.footer-cols{display:flex;gap:70px;padding:30px 0 0 60px;color:#c6d0d8}
.footer-cols h4{font-size:12px;font-weight:900;letter-spacing:1px;color:var(--white);margin-bottom:12px}
.footer-cols ul{list-style:none;font-size:12px;line-height:1.9}
.footer-cols p{font-size:12px;line-height:1.8}
</style>
</head>
<body>

<header class="site-nav">
  <div class="brand"><span class="brand-mark"></span>Nimbrotek</div>
  <ul class="menu">
    <li>WHY NIMBROTEK</li><li>PRODUCTS</li><li>COMMUNITY</li><li>RESOURCES</li><li>TRY NIMBROTEK</li><li>CONTACT US</li>
  </ul>
</header>

<section class="hero">
  <div class="hero-bg" role="img" aria-label="Dark blue backdrop with a faint network of connected points"></div>
  <div class="hero-content">
    <h1>Multi cloud native. Serverless by design.<br>NoOps as a first principle.</h1>
    <p>Nimbrotek is an easy to manage serverless platform for building and running scalable web and mobile applications on any infrastructure. Build once, run anywhere for rapid cloud deployment.</p>
    <div class="hero-actions">
      <span class="btn btn-primary">Why Nimbrotek</span>
      <span class="btn btn-ghost">Try it Free</span>
    </div>
    <div class="cloud-partners">
      <div class="partner"><span class="partner-shape"></span>Gleamcore Cloud</div>
      <div class="partner"><span class="partner-shape"></span>Veltra</div>
      <div class="partner"><span class="partner-shape"></span>Orbix Cloud</div>
      <div class="partner"><span class="partner-shape"></span>Karuna Cloud</div>
      <div class="partner"><span class="partner-shape"></span>Tessor</div>
      <div class="partner"><span class="partner-shape"></span>On-premise</div>
    </div>
  </div>
</section>

<section class="portability">
  <h2>Nimbrotek enables serverless development<br>with application portability</h2>
  <div class="feature-cards">
    <div class="phone-card"><div class="screen">
      <svg width="40" height="40" viewBox="0 0 40 40"><polygon points="20,3 35,11.5 35,28.5 20,37 5,28.5 5,11.5" fill="none" stroke="#1ba1e2" stroke-width="3"/></svg>
      <span class="label">Multi Cloud Migration</span></div></div>
    <div class="phone-card"><div class="screen">
      <svg width="40" height="40" viewBox="0 0 40 40"><circle cx="15" cy="20" r="11" fill="none" stroke="#1ba1e2" stroke-width="3"/><circle cx="25" cy="20" r="11" fill="none" stroke="#5d6b78" stroke-width="3"/></svg>
      <span class="label">Hybrid Cloud</span></div></div>
    <div class="phone-card"><div class="screen">
      <svg width="40" height="40" viewBox="0 0 40 40"><rect x="6" y="6" width="28" height="28" fill="none" stroke="#1ba1e2" stroke-width="3"/><path d="M13 20h14M20 13v14" stroke="#5d6b78" stroke-width="3"/></svg>
      <span class="label">Serverless Platform</span></div></div>
    <div class="phone-card"><div class="screen">
      <svg width="40" height="40" viewBox="0 0 40 40"><circle cx="20" cy="20" r="15" fill="none" stroke="#1ba1e2" stroke-width="3"/><path d="M12 20l6 6 10-12" fill="none" stroke="#5d6b78" stroke-width="3"/></svg>
      <span class="label">NoOps</span></div></div>
  </div>
</section>

<section class="benefits">
  <h2>Nimbrotek benefits developers, operations, and the organization with a serverless platform for multi cloud deployment.</h2>
  <svg class="benefit-map" width="1200" height="260" viewBox="0 0 1200 260" font-family="Lato, Arial, sans-serif">
    <path d="M340 80H860M600 80v100M600 180h0" stroke="#d6dde3" stroke-width="2" fill="none"/>
    <text x="340" y="30" text-anchor="middle" font-size="13" fill="#5d6b78">Efficient Ops</text>
    <text x="600" y="30" text-anchor="middle" font-size="13" fill="#5d6b78">Web/Apps</text>
    <text x="860" y="30" text-anchor="middle" font-size="13" fill="#5d6b78">Multi Cloud</text>
    <circle cx="340" cy="80" r="30" fill="#fff" stroke="#d6dde3" stroke-width="2"/>
    <rect x="326" y="66" width="28" height="28" fill="none" stroke="#1ba1e2" stroke-width="3"/>
    <circle cx="600" cy="80" r="30" fill="#fff" stroke="#d6dde3" stroke-width="2"/>
    <path d="M600 64v12M586 76h28M586 76v12M600 76v12M614 76v12" stroke="#1ba1e2" stroke-width="3" fill="none"/>
    <circle cx="860" cy="80" r="30" fill="#fff" stroke="#d6dde3" stroke-width="2"/>
    <circle cx="851" cy="72" r="6" fill="#1ba1e2"/><circle cx="869" cy="72" r="6" fill="#5d6b78"/><circle cx="851" cy="90" r="6" fill="#5d6b78"/><circle cx="869" cy="90" r="6" fill="#1ba1e2"/>
    <circle cx="600" cy="180" r="30" fill="#fff" stroke="#d6dde3" stroke-width="2"/>
    <path d="M586 192l10-12 8 6 12-16" stroke="#1ba1e2" stroke-width="3" fill="none"/>
    <text x="645" y="185" font-size="13" fill="#5d6b78">Sustained Growth</text>
  </svg>
</section>

<section class="calculator">
  <div class="calc-info">
    <h3>Calculate The Cost<br>To Migrate Cloud</h3>
    <p>Estimate how quickly a serverless move pays back. Adjust your app count and hosting spend to compare the cost of running on one cloud against a portable, multi cloud setup.</p>
    <p>Results update live and can be exported to share with your finance and operations teams.</p>
  </div>
  <div class="calc-chart">
    <svg width="680" height="320" viewBox="0 0 680 320" font-family="Lato, Arial, sans-serif">
      <path d="M40 300 L600 60 L600 300 Z" fill="#4fbbee"/>
      <path d="M40 300 L600 130 L600 300 Z" fill="#2a9ed8"/>
      <path d="M40 300 L600 200 L600 300 Z" fill="#1a7fb8"/>
      <circle cx="600" cy="60" r="5" fill="#fff"/><circle cx="600" cy="130" r="5" fill="#fff"/><circle cx="600" cy="200" r="5" fill="#fff"/>
      <text x="612" y="64" font-size="11" fill="#fff">$48,000</text>
      <text x="612" y="134" font-size="11" fill="#fff">$26,000</text>
      <text x="612" y="204" font-size="11" fill="#fff">$12,000</text>
      <text x="40" y="60" font-size="11" fill="#fff">Cloud hosting spend</text>
      <rect x="150" y="54" width="150" height="4" fill="#fff" opacity=".6"/><circle cx="220" cy="56" r="8" fill="#fff"/>
      <text x="40" y="100" font-size="11" fill="#fff">Number of apps</text>
      <rect x="150" y="94" width="150" height="4" fill="#fff" opacity=".6"/><circle cx="180" cy="96" r="8" fill="#fff"/>
    </svg>
  </div>
</section>

<section class="steps">
  <h2>Get started in 3 easy steps</h2>
  <div class="step-list">
    <div class="step">
      <span class="step-icon"><svg width="20" height="20" viewBox="0 0 20 20"><path d="M4 10l4 4 8-9" stroke="#fff" stroke-width="3" fill="none"/></svg></span>
      <div><h4>ONBOARDING SOLUTIONS</h4><p>Pick a deployment that fits your team and install the platform on any cloud, in minutes.</p></div>
    </div>
    <div class="step">
      <span class="step-icon"><svg width="20" height="20" viewBox="0 0 20 20"><path d="M7 5l-5 5 5 5M13 5l5 5-5 5" stroke="#fff" stroke-width="2.5" fill="none"/></svg></span>
      <div><h4>WRITE YOUR APP</h4><p>Write your application in Python, Java, Go or PHP using the standard APIs you know.</p></div>
    </div>
    <div class="step">
      <span class="step-icon"><svg width="20" height="20" viewBox="0 0 20 20"><path d="M6 4l10 6-10 6z" fill="#fff"/></svg></span>
      <div><h4>RUN YOUR APP</h4><p>Deploy with one command and let the platform scale, heal and balance it for you.</p></div>
    </div>
  </div>
  <span class="btn btn-primary">Install Nimbrotek</span>
</section>

<section class="testimonials">
  <div class="quote-panel">
    <h3>Testimonials</h3>
    <blockquote>“Nimbrotek lets us move our app between clouds without a rewrite. Our team ships faster and spends less time on ops work.”</blockquote>
    <cite>RENA HOLT – Director, Software</cite>
    <div class="quote-nav">
      <span><svg width="10" height="10" viewBox="0 0 10 10"><path d="M7 1L3 5l4 4" stroke="#fff" stroke-width="2" fill="none"/></svg></span>
      <span><svg width="10" height="10" viewBox="0 0 10 10"><path d="M3 1l4 4-4 4" stroke="#fff" stroke-width="2" fill="none"/></svg></span>
    </div>
  </div>
  <div class="video-frame" role="img" aria-label="Video still of the company chief executive speaking in an office">
    <svg class="play" viewBox="0 0 60 60"><circle cx="30" cy="30" r="29" fill="rgba(255,255,255,.25)" stroke="#fff" stroke-width="2"/><path d="M24 18l18 12-18 12z" fill="#fff"/></svg>
    <div class="speaker"><strong>DALE MARROW</strong><span>CEO, NIMBROTEK SYSTEMS</span></div>
  </div>
</section>

<section class="clients">
  <h2>Successful startups and innovative companies choose Nimbrotek</h2>
  <div class="client-row">
    <span class="client">Lumora</span>
    <span class="client"><i></i>Quillex</span>
    <span class="client">Vantrel</span>
    <span class="client">Ferno</span>
    <span class="client">Plexa</span>
  </div>
</section>

<footer class="site-footer">
  <div class="contact-form">
    <h3>Contact Nimbrotek</h3>
    <div class="field">Name</div>
    <div class="field">Email</div>
    <div class="field">Company</div>
    <div class="field tall">Message</div>
    <span class="submit">SUBMIT</span>
  </div>
  <div class="footer-cols">
    <div>
      <h4>NAVIGATION</h4>
      <ul><li>Home</li><li>Why Nimbrotek</li><li>Products</li><li>Community</li><li>Resources</li><li>Try Nimbrotek</li><li>Contact Us</li></ul>
    </div>
    <div>
      <h4>CONTACT</h4>
      <p>88 Harrow Lane<br>Port Elva<br>CA 90000</p>
    </div>
    <div>
      <h4>&nbsp;</h4>
      <p>(555) 014-2288<br>hello@nimbrotek.com</p>
    </div>
  </div>
</footer>

</body>
</html>
```